Real Estate Investing company needs a business card design

We need a business card design for new Real Estate Investment Company called "Bright Harbor Holdings, LLC." We buy homes for cash and close quickly in any situation. Our company provides an easy and fast option for home owners who are in tough situations who need to sell their home fast and don't want realtor fees or other listing hassles. We also renovate and resell our homes which helps provide housing for the community. We would like to see designs that use the colors blue and white to match our company logo or other colors that may match our company logo. The final design should communicate trust and easy process.
Industry/Entity Type
Business
Contact Information for Business Card
Front should have company name and company logo. back of card should have company logo and area to list services.

```html
<!DOCTYPE html>
<html lang="en">
<head>
<meta charset="utf-8">
<title>Bright Harbor Holdings – Business Card</title>
<link rel="stylesheet" href="https://fonts.googleapis.com/css2?family=Ubuntu:wght@500;700&family=Arimo:wght@400&family=PT+Sans:ital@1&display=swap">
<style>
  :root {
    --brand-blue: #0d5fa9;
    --card-white: #eef0f2;
    --ink: #4a4c50;
    --back-text: #e4ecf5;
    --backdrop: #8d8e90;
  }
  * { box-sizing: border-box; margin: 0; padding: 0; }
  html, body { width: 1105px; height: 1200px; overflow: hidden; }
  body { background: var(--backdrop); position: relative; }

  .card {
    position: absolute;
    left: 182px;
    width: 747px;
    height: 427px;
    box-shadow: 0 10px 18px rgba(0,0,0,0.18);
  }
  .card--front { top: 119px; background: var(--card-white); }
  .card--back { top: 637px; background: var(--brand-blue); }

  /* Front */
  .name-band {
    position: absolute;
    left: 0; top: 40px;
    width: 440px; height: 97px;
    background: var(--brand-blue);
    clip-path: polygon(0 0, 100% 0, 92% 100%, 0 100%);
  }
  .person { position: absolute; left: 34px; top: 58px; color: #fff; font-family: "Ubuntu", sans-serif; font-weight: 500; }
  .person__name { font-size: 28px; line-height: 34px; }
  .person__title { font-size: 21px; line-height: 26px; }

  .company-name {
    position: absolute;
    right: 39px; top: 48px;
    display: flex; align-items: center; gap: 12px;
    font-family: "Ubuntu", sans-serif; font-weight: 700;
    color: var(--brand-blue);
    font-size: 31px; line-height: 36px;
    text-align: right;
  }
  .company-name__mark { width: 18px; height: 18px; background: var(--brand-blue); }

  .contact {
    position: absolute; left: 34px; top: 306px;
    list-style: none;
    font-family: "Arimo", sans-serif; font-size: 20px; color: var(--ink);
  }
  .contact li { display: flex; align-items: center; height: 28.5px; }
  .contact svg { width: 20px; height: 20px; margin-right: 9px; fill: var(--brand-blue); }

  .address {
    position: absolute; right: 39px; top: 306px;
    font-family: "Arimo", sans-serif; font-size: 20px; color: var(--ink);
    text-align: right; font-style: normal;
  }
  .address p { height: 28.5px; line-height: 28.5px; }

  /* Back */
  .back-name {
    position: absolute; left: 0; right: 0; top: 92px;
    display: flex; justify-content: center; align-items: center; gap: 14px;
    font-family: "Ubuntu", sans-serif; font-weight: 700;
    color: #fff; font-size: 38px;
  }
  .back-name__mark { width: 22px; height: 22px; background: #fff; }

  .services {
    position: absolute; left: 0; right: 0; top: 204px;
    font-family: "PT Sans", sans-serif; font-style: italic;
    color: var(--back-text); font-size: 18.5px; line-height: 23.5px;
    text-align: center;
  }
  .services p + p { margin-top: 10px; }
</style>
</head>
<body>
  <section class="card card--front" aria-label="Card front">
    <div class="name-band"></div>
    <div class="person">
      <p class="person__name">Daniel Reyes</p>
      <p class="person__title">CEO/Founder</p>
    </div>
    <div class="company-name">
      <span class="company-name__mark"></span>
      <span>Bright Harbor<br>Holdings</span>
    </div>

    <ul class="contact">
      <li>
        <svg viewBox="0 0 20 20" aria-hidden="true"><path d="M4 2l3 0 1.5 4-2 1.5a10 10 0 0 0 6 6l1.5-2 4 1.5 0 3a2 2 0 0 1-2 2A15 15 0 0 1 2 4a2 2 0 0 1 2-2z"/></svg>
        555 214 7730
      </li>
      <li>
        <svg viewBox="0 0 20 20" aria-hidden="true"><rect x="5" y="2" width="10" height="5"/><rect x="1" y="8" width="18" height="7" rx="1"/><rect x="5" y="13" width="10" height="5" fill="#fff" stroke="#0d5fa9" stroke-width="1.5"/></svg>
        555 381 6642
      </li>
      <li>
        <svg viewBox="0 0 20 20" aria-hidden="true"><rect x="2" y="5" width="16" height="11"/><path d="M2 5l8 6 8-6" fill="none" stroke="#fff" stroke-width="1.5"/></svg>
        hello@brightharborhomes.com
      </li>
    </ul>

    <address class="address">
      <p>1420 Cedar Ridge Drive</p>
      <p>Harbor Falls, Maine 04012</p>
      <p>www.brightharborhomes.com</p>
    </address>
  </section>

  <section class="card card--back" aria-label="Card back">
    <div class="back-name">
      <span class="back-name__mark"></span>
      <span>Bright Harbor Holdings</span>
    </div>
    <div class="services">
      <p>We buy homes for cash &amp; close quickly in any situation.</p>
      <p>We provide an easy &amp; fast option for home owners who are<br>in tough situations who need to sell their home fast and don't want<br>realtor fees or other listing hassles.</p>
      <p>We also renovate &amp; resell homes which helps provide<br>housing for the community.</p>
    </div>
  </section>
</body>
</html>
```